Buch-/eBook-Cover für Esoterikbuch
Alle meine Änderungswünsche wurden zeitnah umgesetzt. Als es nach der Dateiübergabe technische Probleme gab, weil ich den Buchinhalt falsch formatiert hatte, hat die Designerin viel Geduld bewiesen und das Cover dann klaglos an die neuen Formate angepasst. Ich werde jederzeit gerne wieder mit ihr zusammenarbeiten.
Zielgruppe
Ebook- und Taschenbuchcover für ein Esoterikbuch über Quantenheilung auf Lesora. Details befinden sich im Anhang.
Aufgabenstellung
Keine besonderen Vorgaben.

```html
<!DOCTYPE html>
<html lang="de">
<head>
<meta charset="utf-8">
<title>Quantenresonanz und Geisteskraft – Cover</title>
<link href="https://fonts.googleapis.com/css2?family=Ubuntu:wght@300;400;700&display=swap" rel="stylesheet">
<style>
  :root {
    --page: #ffffff;
    --cover: #0c0809;
    --ink: #f4f0ee;
    --glow-core: #ffe7b0;
    --glow-orange: #e0782a;
    --glow-magenta: #9a3f6a;
    --glow-deep: #2a1018;
  }
  * { margin: 0; padding: 0; box-sizing: border-box; }
  html, body {
    width: 1200px; height: 1128px; overflow: hidden;
    background: var(--page);
    font-family: "Ubuntu", sans-serif;
  }
  .spread {
    position: absolute; top: 174px; left: 50px;
    display: flex; gap: 60px;
  }
  .cover {
    position: relative; width: 520px; height: 780px;
    background: var(--cover); color: var(--ink);
    overflow: hidden;
  }
  .back-text {
    position: absolute; top: 76px; left: 62px; width: 340px;
    font-weight: 300; font-size: 14.5px; line-height: 2.55;
    text-align: justify; hyphens: auto; -webkit-hyphens: auto;
  }
  .back-text p + p { margin-top: 22px; }
  .back-spine-name {
    position: absolute; top: 40px; right: 18px;
    writing-mode: vertical-rl; font-size: 10px; letter-spacing: 3px;
    font-weight: 300; text-transform: uppercase; opacity: .85;
  }
  .artwork {
    position: absolute; top: 0; left: 0; width: 100%; height: 560px;
    background:
      radial-gradient(circle at 50% 36%, var(--glow-core) 0%, var(--glow-orange) 9%, var(--glow-magenta) 26%, var(--glow-deep) 48%, transparent 70%),
      radial-gradient(ellipse at 50% 45%, rgba(224,120,42,.55) 0%, rgba(60,20,25,.6) 55%, var(--cover) 80%);
  }
  .artwork::after {
    content: ""; position: absolute; inset: auto 0 0 0; height: 120px;
    background: linear-gradient(transparent, var(--cover));
  }
  .author {
    position: absolute; top: 36px; width: 100%; text-align: center;
    font-weight: 400; font-size: 20px; letter-spacing: .5px;
  }
  .title-block {
    position: absolute; top: 552px; width: 100%; text-align: center;
  }
  .title-main {
    font-weight: 700; font-size: 47px; line-height: 1; letter-spacing: .5px;
  }
  .title-sub {
    font-weight: 300; font-size: 44px; line-height: 1.1; margin-top: 4px;
  }
  .tagline {
    font-weight: 300; font-size: 21px; line-height: 1.15; margin-top: 20px;
  }
</style>
</head>
<body>
  <main class="spread">
    <section class="cover cover-back">
      <div class="back-text">
        <p>Willkommen in der subatomaren Welt aus Quarks und Strings, wo reines Bewusstsein und reine Informationen unabhängig von Zeit und Raum das Dasein bestimmen. Seit Jahrhunderten wird die Quantenheilung erfolgreich praktiziert, wenn auch unter anderem Namen. Erst in den letzten Jahren ist es der Wissenschaft gelungen, die Wirkungsweise dieser uralten Heilungsmethode mit modernen Erkenntnissen aus der Quantenphysik in Verbindung zu bringen.</p>
        <p>Die daraus resultierenden Schlussfolgerungen und erweiterten Heilungstechniken wird dieses Buch Ihnen unter Bezug auf die jeweilige Methodik und Verfahrensweisen näher darlegen.</p>
      </div>
      <div class="back-spine-name">Konrad Sternwald</div>
    </section>

    <section class="cover cover-front">
      <div class="artwork" role="img" aria-label="Illustration: meditierende Figur vor leuchtendem kosmischem Energiefeld mit Lichtpunkten in Orange und Magenta"></div>
      <div class="author">KONRAD STERNWALD</div>
      <div class="title-block">
        <h1 class="title-main">QUANTENRESONANZ</h1>
        <div class="title-sub">UND GEISTESKRAFT</div>
        <p class="tagline">WIE SIE DEN ZUGANG ZUR<br>STILLEN FELDEBENE<br>DES LEBENS FINDEN</p>
      </div>
    </section>
  </main>
</body>
</html>
```